K + Claim Advocates Circle Business card

We need to get business card Design for our Company we are Public Adjusters in Chicago Illinois - i like to see good combination and elements from my Company Logo. as well To be an two side design

Target Market(s)

Home /Business owner Property Managers

Industry/Entity Type

Business

Contact Information for Business Card

to show the Element of our logo i will Like 3D

Font styles to use
Sans Serif

Requirements
Must have
• Logo and Element of the Logo in 3D
Nice to have
• Logo That we Provide 3D Same Colors or open for suggestions
Should not have
• unleare view -

```html
<!DOCTYPE html>
<html lang="en">
<head>
<meta charset="utf-8">
<title>Claim Advocates Circle — Stationery</title>
<link href="https://fonts.googleapis.com/css2?family=Oswald:wght@600&family=Open+Sans:wght@400;600&display=swap" rel="stylesheet">
<style>
  :root {
    --bg: #f1f1f1;
    --paper: #fbfbfb;
    --navy: #1c1f4a;
    --blue: #1f45c8;
    --royal: #1d3aa8;
    --red: #c41a1d;
    --ink: #444;
  }
  * { margin: 0; padding: 0; box-sizing: border-box; }
  html, body { width: 1200px; height: 795px; overflow: hidden; background: var(--bg); }
  body { position: relative; font-family: "Open Sans", sans-serif; color: var(--ink); }

  .sheet { position: absolute; background: var(--paper); box-shadow: 0 1px 3px rgba(0,0,0,.12); overflow: hidden; }
  .brand-stripe {
    position: absolute; left: 0; right: 0; bottom: 0; height: 6px;
    background: linear-gradient(100deg, var(--navy) 0%, var(--blue) 60%, var(--blue) 77.5%, #fff 77.5%, #fff 78.5%, var(--red) 78.5%);
  }

  .brand { display: flex; flex-direction: column; align-items: center; gap: 4px; }
  .brand-dot { border-radius: 50%; background: var(--royal); }
  .brand-name { font-family: "Oswald", sans-serif; font-weight: 600; color: var(--royal); white-space: nowrap; letter-spacing: .2px; }

  /* Letterhead */
  .letterhead { left: 293px; top: 99px; width: 292px; height: 415px; }
  .letterhead .brand { position: absolute; top: 26px; left: 0; right: 0; }
  .letterhead .brand-dot { width: 26px; height: 26px; }
  .letterhead .brand-name { font-size: 8px; }
  .letterhead .footer { position: absolute; bottom: 16px; left: 0; right: 0; text-align: center; font-size: 4.2px; line-height: 8px; color: #555; }
  .contact-row { display: flex; justify-content: center; gap: 5px; }
  .contact-row span { display: inline-flex; align-items: center; gap: 2px; }
  .icon { width: 4px; height: 4px; fill: var(--royal); }

  /* Presentation folder */
  .folder { left: 636px; top: 80px; width: 346px; height: 437px; background: radial-gradient(ellipse at 50% 58%, #1d4fe0 0%, #1a33a0 40%, var(--navy) 85%); }
  .folder .brand { position: absolute; top: 200px; left: 0; right: 0; gap: 10px; }
  .folder .brand-dot { width: 44px; height: 44px; background: #fff; }
  .folder .brand-name { color: #fff; font-size: 15px; }
  .folder .brand-stripe { height: 6px; background: linear-gradient(100deg, #fff 0%, #fff 80%, var(--red) 80%); }

  /* Business cards */
  .card { width: 132px; height: 75px; }
  .card-front { left: 187px; top: 551px; }
  .card-front .brand { position: absolute; left: 6px; top: 16px; width: 58px; gap: 3px; }
  .card-front .brand-dot { width: 16px; height: 16px; }
  .card-front .brand-name { font-size: 4.6px; }
  .card-front .divider { position: absolute; left: 70px; top: 12px; width: 1px; height: 48px; background: #ccc; }
  .card-front .details { position: absolute; left: 76px; top: 12px; font-size: 3px; line-height: 4.3px; color: #555; }
  .card-front .person { font-size: 4.6px; font-weight: 600; color: var(--royal); line-height: 5px; }
  .card-front .role { color: var(--red); margin-bottom: 3px; }
  .card-front .brand-stripe { height: 5px; }
  .card-back { left: 187px; top: 647px; background: var(--red); }
  .card-back .brand { position: absolute; top: 18px; left: 0; right: 0; gap: 6px; }
  .card-back .brand-dot { width: 22px; height: 22px; background: #fff; }
  .card-back .web { color: #fff; font-size: 3.8px; letter-spacing: .3px; }

  /* Envelopes */
  .envelope { width: 328px; height: 156px; }
  .envelope-front { left: 354px; top: 562px; }
  .envelope-front .brand { position: absolute; left: 14px; top: 14px; width: 60px; gap: 3px; }
  .envelope-front .brand-dot { width: 20px; height: 20px; }
  .envelope-front .brand-name { font-size: 5.4px; }
  .envelope-front .return { position: absolute; left: 14px; top: 125px; font-size: 4.4px; line-height: 6px; color: #555; }
  .envelope-back { left: 714px; top: 562px; }
  .envelope-back .flap {
    position: absolute; left: 0; top: 0; width: 328px; height: 56px;
    background: radial-gradient(ellipse at 50% 40%, #1d4fe0 0%, #1a2f8c 55%, var(--navy) 100%);
    clip-path: polygon(0 0, 100% 0, 97% 100%, 3% 100%);
  }
  .envelope-back .brand { position: absolute; top: 12px; left: 0; right: 0; gap: 5px; }
  .envelope-back .brand-dot { width: 18px; height: 18px; background: #fff; }
  .envelope-back .web { color: #c8d2ff; font-size: 3.6px; letter-spacing: .3px; }
</style>
</head>
<body>

<svg width="0" height="0" style="position:absolute">
  <symbol id="ico-phone" viewBox="0 0 10 10"><path d="M2 1l2 2-1 1.3c.6 1.2 1.5 2.1 2.7 2.7L7 6l2 2-1.2 1.3C4.5 9 1 5.5.7 2.2z"/></symbol>
  <symbol id="ico-mail" viewBox="0 0 10 10"><rect x="0" y="2" width="10" height="6"/></symbol>
  <symbol id="ico-web" viewBox="0 0 10 10"><circle cx="5" cy="5" r="4.5"/></symbol>
</svg>

<section class="sheet letterhead">
  <div class="brand">
    <span class="brand-dot"></span>
    <span class="brand-name">Claim Advocates Circle, Inc.</span>
  </div>
  <div class="footer">
    <div>4120 Larkspur Court, Fairbanks, Alaska 39812</div>
    <div class="contact-row">
      <span><svg class="icon"><use href="#ico-phone"/></svg>555 204 7781</span>
      <span><svg class="icon"><use href="#ico-phone"/></svg>555 318 4470</span>
      <span><svg class="icon"><use href="#ico-phone"/></svg>555 692 1185</span>
      <span><svg class="icon"><use href="#ico-mail"/></svg>mail@claimadvocates.com</span>
      <span><svg class="icon"><use href="#ico-web"/></svg>claimadvocates.com</span>
    </div>
  </div>
  <div class="brand-stripe"></div>
</section>

<section class="sheet folder">
  <div class="brand">
    <span class="brand-dot"></span>
    <span class="brand-name">Claim Advocates Circle, Inc.</span>
  </div>
  <div class="brand-stripe"></div>
</section>

<section class="sheet card card-front">
  <div class="brand">
    <span class="brand-dot"></span>
    <span class="brand-name">Claim Advocates Circle, Inc.</span>
  </div>
  <div class="divider"></div>
  <div class="details">
    <div class="person">DANA WHITFIELD</div>
    <div class="role">CEO / Founder</div>
    <div>4120 Larkspur Court</div>
    <div>Fairbanks, Alaska 39812</div>
    <div>555 204 7781</div>
    <div>555 318 4470</div>
    <div>555 692 1185</div>
    <div>mail@claimadvocates.com</div>
    <div>www.claimadvocates.com</div>
  </div>
  <div class="brand-stripe"></div>
</section>

<section class="sheet card card-back">
  <div class="brand">
    <span class="brand-dot"></span>
    <span class="web">www.ClaimAdvocatesCircle.com</span>
  </div>
</section>

<section class="sheet envelope envelope-front">
  <div class="brand">
    <span class="brand-dot"></span>
    <span class="brand-name">Claim Advocates Circle, Inc.</span>
  </div>
  <div class="return">
    <div>4120 Larkspur Court</div>
    <div>Fairbanks, Alaska 39812</div>
  </div>
  <div class="brand-stripe"></div>
</section>

<section class="sheet envelope envelope-back">
  <div class="flap">
    <div class="brand">
      <span class="brand-dot"></span>
      <span class="web">www.ClaimAdvocatesCircle.com</span>
    </div>
  </div>
</section>

</body>
</html>
```